Flyer für Logopädie, Ergo- und Physiotherapie
Zielgruppe
Logopädie, Ergotherapie, Physiotherapie, K-Vela, Fitness
Aufgabenstellung
Ich lade den alten Flyer für die Texte hoch. Dieser ist im Moment DIN lang (99 x 210 mm). Die Homepage, Flyer und die alte Praxis(wir sind umgezogen) war komplett grün gehalten. Davon sind wir abgekommen. Grün sollte es nicht mehr sein. Die Praxis ist nun mehr Braun, viel Holz, edler. Wir sind eine aktive Praxis, es soll nicht nach Wellness aussehen. Die Farben des 'Balls' aus unserem Logo soll sich nicht verändern. Ich habe Bilder vom Gebäude der Praxis hochgeladen. Falls möglichl, kann man hier unser Logo oder nur den Ball mit einfügen?
Die Adresse auf dem Flyer stimmt nicht mehr.
Lenzbacher-Weg-Str. 4
91347 Kornhain

```html
<!DOCTYPE html>
<html lang="de">
<head>
<meta charset="utf-8">
<title>Lindenhof Therapie Flyer</title>
<link href="https://fonts.googleapis.com/css2?family=Poppins:wght@400;500;600;700&display=swap" rel="stylesheet">
<style>
:root{
  --brown:#6e4524;
  --tan:#d9c2a0;
  --tan-text:#a9855e;
  --cream:#f2e8d9;
  --cream-deep:#ecdfc9;
  --white:#ffffff;
  --ink:#3b2a1d;
  --bg:#9c9c9c;
}
*{margin:0;padding:0;box-sizing:border-box}
html,body{width:803px;height:1200px;overflow:hidden}
body{background:var(--bg);font-family:"Poppins",sans-serif;color:var(--ink);position:relative}
.spread{position:absolute;left:20px;width:763px;height:545px;display:grid;grid-template-columns:repeat(3,1fr);overflow:hidden;background:var(--white);box-shadow:0 2px 8px rgba(0,0,0,.25)}
.spread--outside{top:40px}
.spread--inside{top:615px}
.panel{position:relative;padding:0 14px;overflow:hidden}
.panel--cream{background:var(--cream)}
.photo{position:absolute;left:12px;right:12px;border-radius:2px}
.brand{display:flex;align-items:center;justify-content:space-between;gap:8px}
.brand__name{font-weight:700;color:var(--brown);font-size:15px;line-height:1.15}
.brand__dot{flex:none;width:44px;height:44px;border-radius:50%;background:var(--cream-deep);border:2px solid var(--tan)}
.pill{background:var(--brown);color:var(--white);font-weight:600;font-size:12px;text-align:center;border-radius:14px;padding:4px 0;line-height:1.2}
.list{list-style:none;font-size:7.3px;line-height:1.45}
.list li{position:relative;padding-left:11px}
.list li::before{content:"";position:absolute;left:0;top:3px;width:5px;height:5px;border-radius:50%;border:1.6px solid var(--brown)}
.list b{font-weight:700}
.list--spaced li{margin-bottom:5px}
.lead{font-size:7.3px;line-height:1.4}
.h-brown{color:var(--brown);font-weight:700}
.box{border:2px solid var(--tan);border-radius:10px;background:var(--white);text-align:center}
.waves{position:absolute;left:0;bottom:0;width:763px}
.on-brown{position:absolute;color:var(--white);font-weight:700}
</style>
</head>
<body>

<section class="spread spread--outside">
  <div class="panel">
    <div class="brand" style="margin-top:18px">
      <div class="brand__name">Lindenhof<br>Therapie</div>
      <div class="brand__dot"></div>
    </div>
    <div class="photo" role="img" aria-label="Heller Trainingsraum mit Gymnastikbällen und Schreibtisch" style="top:90px;height:130px;left:0;right:0;background:linear-gradient(160deg,#f4f4f2,#d9dedd 55%,#8fb7b0)"></div>
    <div class="box" style="position:absolute;top:205px;left:12px;right:12px;padding:10px 6px 8px">
      <div class="h-brown" style="font-size:14px;line-height:1.1">Unsere Leistungen</div>
      <div style="font-size:7px;margin-top:2px">• EINFACH • SICHER • EFFEKTIV</div>
      <div class="h-brown" style="font-size:14px;margin-top:10px">FIT IN 35 MINUTEN.</div>
      <div style="font-size:7.5px;line-height:1.35;margin-top:2px">MEHR VITALITÄT<br>MEHR SCHMERZFREIHEIT<br>MEHR WOHLBEFINDEN</div>
    </div>
    <div style="position:absolute;top:362px;left:0;right:0;text-align:center">
      <div style="font-size:8px">VEREINBAREN SIE EIN</div>
      <div class="h-brown" style="font-size:17px;line-height:1.1">KOSTENLOSES<br>PROBETRAINING</div>
    </div>
  </div>

  <div class="panel panel--cream">
    <div class="pill" style="margin-top:18px">Unsere Leistungen</div>
    <ul class="list" style="margin-top:8px">
      <li>Physiotherapie/ Krankengymnastik</li>
      <li>Logopädie und Ergotherapie</li>
      <li>Behandlung von Kindern und Erwachsenen</li>
      <li>Hausbesuche/ Heimbesuche</li>
      <li>alle Krankenkassen sowie Privat</li>
      <li>Training im Vitalon-Gesundheitszirkel</li>
      <li>personal Training</li>
    </ul>
    <div style="margin-top:14px;border:1.5px solid var(--tan);border-radius:10px;padding:8px 4px 6px;text-align:center">
      <div class="h-brown" style="font-size:11px;margin-top:-2px">Öffnungszeiten</div>
      <div style="font-size:7.5px;line-height:1.4">Montag - Freitag 08.00-20.00 Uhr<br>Samstag 08.00-12.00 Uhr</div>
    </div>
    <div class="pill" style="margin-top:14px">Warum Lindenhof?</div>
    <ul class="list" style="margin-top:8px">
      <li>Fachlich kompetente Therapeuten</li>
      <li>kostenfreie Parkplätze direkt vor der Tür</li>
      <li>sehr gute Erreichbarkeit von Westfeld und Talbrück über die Autobahn (je ca. 5 Min.)</li>
      <li>auch mit öffentlichen Verkehrsmitteln sehr gut erreichbar!</li>
      <li>Therapiezentrum mit Physio, Logo &amp; Ergo</li>
      <li>Familienunternehmen mit einer herzlichen und fröhlichen Atmosphäre!!!</li>
    </ul>
  </div>

  <div class="panel">
    <div class="brand" style="margin-top:18px">
      <div class="brand__name">Lindenhof<br>Therapie</div>
      <div class="brand__dot"></div>
    </div>
    <div class="photo" role="img" aria-label="Praxisgebäude mit Parkplatz" style="top:78px;height:135px;left:0;right:0;background:linear-gradient(180deg,#d5e2ee,#e9ecef 40%,#8b8f93 75%,#5b5f63)"></div>
    <div style="position:absolute;top:232px;left:0;right:0;text-align:center;color:var(--brown);font-weight:700;font-size:10px;line-height:1.3">Lenzbacher-Weg-Str. 4<br>91347 Kornhain</div>
    <div class="box" style="position:absolute;top:270px;left:22px;right:22px;padding:5px 4px">
      <div class="h-brown" style="font-size:12.5px;line-height:1.3">Tel: 09876 - 543 21 21<br>Fax: 09876 - 543 21 22</div>
    </div>
    <div style="position:absolute;top:328px;left:0;right:0;text-align:center;font-weight:700;font-size:8.5px;line-height:1.35">Internet: www.lindenhof-therapie.de<br>Email: info@lindenhof-therapie.de</div>
  </div>

  <svg class="waves" viewBox="0 0 763 130" preserveAspectRatio="none" aria-hidden="true" style="height:130px">
    <path d="M0 40 C120 70 250 10 400 40 S650 60 763 30 V130 H0Z" fill="#d9c2a0"/>
    <path d="M0 52 C120 82 250 22 400 52 S650 72 763 42 V130 H0Z" fill="#ffffff"/>
    <path d="M0 68 C130 95 260 40 400 66 S650 85 763 58 V130 H0Z" fill="#6e4524"/>
  </svg>
  <div style="position:absolute;left:262px;top:418px;width:86px;height:86px;border-radius:50%;background:var(--cream-deep);border:3px solid var(--tan)"></div>
  <div class="on-brown" style="left:509px;width:254px;bottom:14px;text-align:center;line-height:1.25">
    <div style="font-size:13px">Inhaber:</div>
    <div style="font-size:10px">Lena und Jonas Brunner</div>
  </div>
</section>

<section class="spread spread--inside">
  <div class="panel">
    <div class="photo" role="img" aria-label="Therapeutin am Schreibtisch in der Praxis" style="top:14px;height:102px;background:linear-gradient(135deg,#6d7178,#c9c6c0 45%,#f1efea)"></div>
    <div class="pill" style="position:absolute;top:104px;left:22px;right:22px">Logopädie</div>
    <div style="position:absolute;top:136px;left:14px;right:10px">
      <p class="lead">Therapie von Stimm-, Sprech-, Sprachund Schluckstörungen bei Kindern und Erwachsenen.</p>
      <ul class="list list--spaced" style="margin-top:6px">
        <li><b>Sprachentwicklungsstörung</b><br>Probleme bei der Aussprache, in der Grammatik, im Wortschatz,im Sprachverständnis</li>
        <li><b>Therapie nach Alvarado Ruiz</b><br>z.B. Therapie für Kinder mit genetischen Syndromen oder bei Fütter- , Saug- und Essproblemen im Säuglings- und Kleinkindalter</li>
        <li><b>falsches/ viscerales Schluckmuster</b><br>Zunge drückt gegen die Zähne</li>
        <li><b>Dysphonie - Stimmstörung</b><br>Stimme ist heiser ohne Erkältung</li>
        <li><b>Dysphagie - Schluckstörung</b><br>häufiges Verschlucken, husten beim Essen/ Trinken</li>
        <li><b>Aphasie - nach Schlaganfall häufig</b><br>Störung d. Sprache, des Sprechens, des Lesens, des Schreibens, der Wortfindung od. des Sprachverständnisses</li>
        <li><b>Dysarthrie - Störung der Sprechmotorik</b><br>Lähmung der Gesichtsmuskulatur, Probleme beim Sprechen durch Zungenlähmung</li>
      </ul>
    </div>
  </div>

  <div class="panel panel--cream">
    <div class="photo" role="img" aria-label="Behandlungsraum mit grüner Therapieliege" style="top:14px;height:102px;background:linear-gradient(135deg,#e9ece8,#b9bdb6 50%,#8cc84b)"></div>
    <div class="pill" style="position:absolute;top:104px;left:22px;right:22px">Physiotherapie</div>
    <div style="position:absolute;top:136px;left:14px;right:10px">
      <p class="lead">Verbesserung der Bewegungs- und Funktionsfähigkeit des menschlichen Körpers, der Muskeln, des Bewegungsapparates, der Wirbelsäule, des Gangbildes durch unterschiedliche therapeutische Maßnahmen.</p>
      <div class="h-brown" style="font-size:12px;margin-top:8px">Behandlungsangebot</div>
      <ul class="list" style="margin-top:4px;font-size:7.8px">
        <li>Manuelle Therapie</li>
        <li>Krankengymnastik</li>
        <li>Krankengymnastik am Gerät</li>
        <li>Krankengymnastik nach Berndtsen für Erwachsene</li>
        <li>Kiefergelenksbehandlung (CMD)</li>
        <li>Manuelle Lymphdrainage</li>
        <li>Klassische Massage</li>
        <li>Bindegewebsmassage</li>
        <li>Beckenbodentraining</li>
        <li>Wärmetherapie (Infrarotbestrahlung)</li>
        <li>Warmpackung (Fango)</li>
        <li>Heiße Rolle</li>
        <li>Kälteanwendung</li>
      </ul>
      <div style="font-weight:700;font-size:9.5px;text-align:center;margin-top:14px;line-height:1.3;color:var(--tan-text)">Alle Leistungen sind auch als<br>Gutschein erhältlich.</div>
    </div>
  </div>

  <div class="panel">
    <div class="photo" role="img" aria-label="Ergotherapieraum mit bunten Bodenmatten und Hängematte" style="top:14px;height:102px;background:linear-gradient(135deg,#f3f0ea,#e3d9c8 45%,#f0c640 70%,#3aa0d8)"></div>
    <div class="pill" style="position:absolute;top:104px;left:22px;right:22px">Ergotherapie</div>
    <div style="position:absolute;top:136px;left:14px;right:10px">
      <p class="lead">Verbesserung gestörter oder verloren gegangener Fähigkeiten wie Grob- und Feinmotorik, Konzentration, Ausdauer, Koordination sowie sozialer und emotionaler Kompetenzen.</p>
      <div class="h-brown" style="font-size:9.5px;margin-top:9px;line-height:1.2">Wir behandeln Kinder und<br>Erwachsene in den Bereichen:</div>
      <ul class="list list--spaced" style="margin-top:6px">
        <li><b>Motorisch- funktionelle Behandlung</b><br>aktive und passive Bewegungsstörung - Störung der Grob- und Feinmotorik - Störung der Haltung</li>
        <li><b>Psychisch-funktionelle Behandlung</b><br>Funktionsstörung der Orientierung zu Raum, Zeit und Person - des Antriebs und des Willens - des Realitätsbewusstseins und der Selbsteinschätzung</li>
        <li><b>Sensomotorisch- perzeptive Behandlung</b><br>Störung der Wahrnehmung - der Körperbewegung - der Koordination</li>
        <li><b>Hirnleistungstraining</b><br>Störung der Konzentration - des Gedächtnisses - der Handlungsplanung</li>
      </ul>
    </div>
    <div class="brand" style="position:absolute;left:14px;right:14px;top:430px">
      <div class="brand__name">Lindenhof<br>Therapie</div>
      <div class="brand__dot"></div>
    </div>
  </div>

  <svg class="waves" viewBox="0 0 763 90" preserveAspectRatio="none" aria-hidden="true" style="height:90px">
    <path d="M0 22 C200 40 420 20 600 18 S720 10 763 6 V90 H0Z" fill="#d9c2a0"/>
    <path d="M0 30 C200 48 420 28 600 26 S720 18 763 14 V90 H0Z" fill="#ffffff"/>
    <path d="M0 42 C200 58 420 38 600 36 S720 28 763 24 V90 H0Z" fill="#6e4524"/>
  </svg>
  <div class="on-brown" style="left:20px;bottom:10px;line-height:1.25">
    <div style="font-size:13px">Tel: 09876 - 543 21 21</div>
    <div style="font-size:7.5px;font-weight:500;padding-left:18px">Internet: www.lindenhof-therapie.de</div>
  </div>
</section>

</body>
</html>
```